Hi,

I have just started up a business called VOLMIRA in Melbourne. We run fun street art tours around Melbourne's CBD.

I need to create a design for the back side of my business cards. I have designed the front side (simply with my logo) however, I am having trouble designing the reverse side in a professional manner. I have attached pictures of what I have done.

The picture attached titled "VOLMIRA Business Cards Back" has all the information that I require on the back side of my business cards; although displayed in an amateur and simple way. As displayed in the picture, I need: the VOLMIRA logo, the website URL, the booking details (phone - 0468 152 837 & email - bookings@volmira-example.com.au) and the service description ($20, One Hour, Tours Daily, Meet at Halberton St Station). I would also like to use the font in the picture supplied which is "source-sans-pro".

The VOLMIRA tours are for tourists and are relaxed, entertaining and fun! I would like the design to reflect this.

Target Market(s)

Backpackers & University Students

Industry/Entity Type

Business

Requirements
Must have
• The VOLMIRA logo, the website URL, the booking details (phone - 0468 152 837 & email - bookings@volmira-example.com.au) and the service description ($20, One Hour, Tours Daily, Meet at Halberton St Station).

```html
<!DOCTYPE html>
<html lang="en">
<head>
<meta charset="utf-8">
<title>VOLMIRA Business Cards</title>
<link rel="stylesheet" href="https://fonts.googleapis.com/css2?family=Jost:wght@400;600&display=swap">
<style>
  :root {
    --backdrop: #e3e3e3;
    --card-light: #f4f4f4;
    --card-edge: #c2c2c2;
    --ink: #111111;
    --band: #1c1c1c;
    --band-text: #ffffff;
  }
  * { box-sizing: border-box; margin: 0; padding: 0; }
  html, body {
    width: 1200px; height: 800px; overflow: hidden;
    background: var(--backdrop);
    font-family: "Jost", "Century Gothic", sans-serif;
    color: var(--ink);
  }
  .canvas { position: relative; width: 1200px; height: 800px; }
  .card {
    position: absolute; left: 332px; width: 536px; height: 310px;
    background: radial-gradient(ellipse at 50% 45%, var(--card-light) 0%, #dcdcdc 55%, var(--card-edge) 100%);
    overflow: hidden;
  }
  .card--front { top: 82px; }
  .card--back { top: 426px; }

  .brand-name { position: absolute; font-weight: 600; letter-spacing: 1px; line-height: 1; }
  .card--front .brand-name { left: 0; right: 0; top: 102px; text-align: center; font-size: 54px; }
  .tagline { position: absolute; left: 0; right: 0; top: 190px; text-align: center; font-size: 22px; line-height: 28px; }
  .tagline strong { font-weight: 600; display: block; }

  .card--back .brand-name { left: 68px; top: 40px; font-size: 28px; }
  .web-band {
    position: absolute; left: 278px; top: 40px; width: 258px; height: 28px;
    background: var(--band); color: var(--band-text);
    font-size: 16px; line-height: 28px; padding-left: 8px; white-space: nowrap;
  }
  .web-band b { font-weight: 600; }

  .facts { position: absolute; top: 0; left: 0; width: 100%; height: 100%; }
  .fact { position: absolute; font-size: 22px; line-height: 29px; text-transform: uppercase; }
  .fact--price { left: 25px; top: 143px; font-weight: 600; }
  .fact--days { left: 138px; top: 128px; }
  .fact--length { left: 266px; top: 128px; font-weight: 600; }
  .fact--meet { left: 386px; top: 114px; font-size: 20px; white-space: nowrap; }

  .booking-band {
    position: absolute; left: 0; bottom: 0; width: 100%; height: 91px;
    background: linear-gradient(180deg, #2a2a2a, var(--band) 60%, #141414);
    color: var(--band-text); text-align: center;
    font-size: 19px; line-height: 23px; padding-top: 9px;
  }
  .booking-band b { font-weight: 600; }
</style>
</head>
<body>
<main class="canvas">
  <section class="card card--front" aria-label="Card front">
    <div class="brand-name">VOLMIRA</div>
    <p class="tagline"><strong>MELBOURNE STREET ART</strong>WALKING TOURS</p>
  </section>

  <section class="card card--back" aria-label="Card back">
    <div class="brand-name">VOLMIRA</div>
    <div class="web-band">www.<b>volmira-example</b>.com.au</div>
    <div class="facts">
      <p class="fact fact--price">$20.00</p>
      <p class="fact fact--days">Tours<br>Daily</p>
      <p class="fact fact--length">One<br>Hour</p>
      <p class="fact fact--meet">Meet at<br>Halberton St<br>Station</p>
    </div>
    <div class="booking-band">
      <p>CALL NIKO TO <b>BOOK NOW</b></p>
      <p>0468 152 837</p>
      <p>bookings@volmira-example.com.au</p>
    </div>
  </section>
</main>
</body>
</html>
```